Looking for a clean, modern, and professional business card design that reflects Valtrim Systems

The design should include the company logo, contact details, and align with our brand identity. Please use a sophisticated and minimalist style, incorporating [specific colors, if applicable]. Creativity is welcome, but the card must maintain a polished and professional appearance.

Details to Include:

Name: Gavin Trelowe
Title: VP Sales / Operations
Company: Valtrim Systems
Phone: 483.216.7705
Email: gavin@valtrimsystems-example.com
Website: www.valtrimsystems-example.com

```html
<!DOCTYPE html>
<html lang="en">
<head>
<meta charset="utf-8">
<title>Valtrim Systems — Business Card</title>
<link rel="stylesheet" href="https://fonts.googleapis.com/css2?family=Montserrat:wght@300;400;700&display=swap">
<style>
  :root {
    --backdrop: #9b9b9b;
    --backdrop-divide: #8f8f8f;
    --card: #050505;
    --card-sheen: #1a1a1a;
    --ink: #ffffff;
    --ink-soft: #e6e6e6;
    --rule: #d9d9d9;
  }
  * { margin: 0; padding: 0; box-sizing: border-box; }
  html, body {
    width: 900px;
    height: 1200px;
    overflow: hidden;
  }
  body {
    position: relative;
    background: linear-gradient(to bottom, var(--backdrop) 0 620px, var(--backdrop-divide) 620px 1200px);
    font-family: "Montserrat", Arial, sans-serif;
    color: var(--ink);
  }
  .card {
    position: absolute;
    left: 140px;
    width: 620px;
    height: 354px;
    border-radius: 22px;
    background: linear-gradient(160deg, var(--card-sheen) 0%, var(--card) 45%, var(--card) 100%);
    box-shadow: 0 18px 40px rgba(0, 0, 0, 0.35);
    overflow: hidden;
  }
  .card--front { top: 130px; }
  .card--back { top: 720px; }

  .wordmark {
    display: flex;
    align-items: center;
    gap: 12px;
    font-weight: 700;
    text-transform: uppercase;
    letter-spacing: 0.08em;
    color: var(--ink);
    white-space: nowrap;
  }
  .wordmark__square {
    width: 16px;
    height: 16px;
    background: var(--ink);
    flex: none;
  }
  .card--front .wordmark {
    position: absolute;
    left: 50%;
    top: 50%;
    transform: translate(-50%, -50%);
    font-size: 34px;
  }
  .card--back .wordmark {
    position: absolute;
    left: 56px;
    top: 48px;
    font-size: 24px;
  }
  .card--back .wordmark__square { width: 12px; height: 12px; }

  .rule {
    position: absolute;
    height: 1.5px;
    background: var(--rule);
  }
  .rule--top { left: 56px; right: 40px; top: 96px; }
  .rule--bottom { left: 40px; width: 400px; bottom: 52px; }

  .person {
    position: absolute;
    left: 0;
    width: 100%;
    top: 118px;
    text-align: center;
  }
  .person__name {
    font-weight: 700;
    font-size: 25px;
    letter-spacing: 0.01em;
  }
  .person__title {
    font-weight: 300;
    font-size: 25px;
    margin-top: 4px;
  }

  .contact {
    position: absolute;
    left: 250px;
    width: 300px;
    top: 220px;
    text-align: center;
    font-weight: 400;
    font-size: 12.5px;
    line-height: 1.45;
    color: var(--ink-soft);
    list-style: none;
  }
</style>
</head>
<body>
  <section class="card card--front" aria-label="Business card front">
    <div class="wordmark"><span class="wordmark__square"></span>Valtrim Systems</div>
  </section>

  <section class="card card--back" aria-label="Business card back">
    <div class="wordmark"><span class="wordmark__square"></span>Valtrim Systems</div>
    <div class="rule rule--top"></div>
    <div class="person">
      <p class="person__name">Gavin Trelowe</p>
      <p class="person__title">VP Sales / Operations</p>
    </div>
    <ul class="contact">
      <li>Valtrim Systems</li>
      <li>gavin@valtrimsystems-example.com</li>
      <li>483.216.7705</li>
      <li>www.valtrimsystems-example.com</li>
    </ul>
    <div class="rule rule--bottom"></div>
  </section>
</body>
</html>
```